Website Velmora Athletics

Velmora Athletics needs an update for our corporate website www.velmoraathletics.example.
We feel the current website is too cluttered with various bits and pecies and strive to a more simpler, easier to navigate website.
We encourage designers to start with a blank canvas, but few aspects of the current website should remain:
- The four lines of business: Sports Media Services, Sports Content Services, Sports Event Services and Sports Federation Services should have a central place on the new site.
- The colour scheme of our house style (black, white and grey/silver) needs to be honoured.
- Our logo should remain as it is (with background intact). Focus on our preferred company logo, found here: http://www.velmoraathletics.example/download/logos/JPEG/VA_logo_on_white.jpg
- A place where visitors can view the latest company headlines. Only the headlines will suffice.
- It should be clear that Velmora Athletics is a sports company. An inventive way of linking our ability of providing sports data with sports images would highly appreciated.
All other components of the current website can remain or be removed/tweaked as the designer pleases. We are open to a complete new look and feel.
A redesign of the homepage should have your focus, but it would be great if the frame work of the design is usable for the other pages of our website as well.
Velmora Athletics keywords that reflect on our company: fast, accurate, innovative, intelligent, no-nonsense, business-aimed, passionate about sports, global, modern.
Target Market(s)
international media (tv stations, newspapers), sports federations, olympic committees, sports results websites, sport app builders

```html
<!DOCTYPE html>
<html lang="en">
<head>
<meta charset="utf-8">
<title>Velmora Athletics</title>
<link rel="stylesheet" href="https://fonts.googleapis.com/css2?family=Arimo:wght@400;700&display=swap">
<style>
:root{
  --page:#ffffff;
  --frame:#dedede;
  --services:#666666;
  --news:#c6c6c6;
  --ink:#1c1c1c;
  --text-soft:#333333;
  --footer-text:#6e6e6e;
  --white:#ffffff;
  --rule:#d8d8d8;
}
*{margin:0;padding:0;box-sizing:border-box}
html,body{width:976px;height:1200px;overflow:hidden;background:var(--page)}
body{position:relative;font-family:"Arimo",Arial,sans-serif;color:var(--ink)}
.site-header{position:absolute;left:0;top:0;width:976px;height:170px}
.header-shapes{position:absolute;left:0;top:0}
.main-nav{position:absolute;top:48px;left:0;width:976px;height:20px}
.main-nav a{position:absolute;color:var(--white);font-weight:700;font-size:15px;text-decoration:none}
.brand-bar{position:absolute;left:32px;top:76px;width:918px;height:82px;border-radius:4px;overflow:hidden;
  background:linear-gradient(90deg,#d9d9d9 0%,#bdbdbd 22%,#7c7c7c 40%,#3a3a3a 50%,#2a2a2a 100%)}
.stadium-photo{position:absolute;left:440px;top:0;width:478px;height:82px;
  background:linear-gradient(90deg,rgba(42,42,42,0) 0%,#3a3a3a 35%,#555555 70%,#3c3c3c 100%)}
.brand-name{position:absolute;left:34px;top:18px;font-weight:700;font-size:36px;color:#111;letter-spacing:.5px}

.content-frame{position:absolute;left:32px;top:178px;width:918px;height:1012px;background:var(--frame);border-radius:3px}

.services{position:absolute;left:46px;top:191px;width:890px;height:413px;background:var(--services);border-radius:4px}
.service{position:absolute;left:18px;width:854px;height:100px;color:var(--white)}
.service h2{font-weight:400;font-size:24px;line-height:28px}
.service p{font-size:17px;line-height:22px;margin-top:2px}
.service .read-more{display:block;font-size:11px;color:var(--white);text-decoration:none;margin-top:3px}
.service-divider{position:absolute;left:18px;width:854px;height:1px;background:var(--rule)}
.partners{position:absolute;right:0;top:6px;display:flex;gap:7px}
.partner-badge{width:62px;height:43px;background:var(--white);border:1px solid #999;display:flex;align-items:center;justify-content:center}
.partner-badge span{display:block;width:30px;height:24px;background:#b8b8b8;border-radius:3px}

.headlines{position:absolute;left:46px;top:616px;width:890px;height:461px;background:var(--news);border-radius:4px}
.news-item{position:absolute;left:19px;width:660px;height:140px}
.news-photo{position:absolute;left:0;top:0;width:147px;height:98px}
.news-item h3{position:absolute;left:167px;top:-1px;font-size:17px;font-weight:700;letter-spacing:.4px}
.news-item p{position:absolute;left:167px;top:24px;width:472px;font-size:11px;line-height:13.6px;letter-spacing:.4px;color:var(--text-soft)}
.events{position:absolute;left:693px;top:25px;width:180px}
.events h3{font-size:15px;font-weight:700;line-height:18px;letter-spacing:.3px}
.event{margin-top:24px}
.events h3 + .event{margin-top:22px}
.event h4{font-size:12px;color:var(--white);font-weight:700;margin-bottom:6px;letter-spacing:.3px}
.event p{font-size:10.5px;line-height:14px;color:var(--text-soft);letter-spacing:.2px}

.site-footer{position:absolute;left:32px;top:1085px;width:918px;height:105px}
.follow{position:absolute;left:31px;top:6px;font-size:11px;color:#333}
.social{position:absolute;left:31px;top:22px;display:flex;gap:11px}
.social span{width:21px;height:21px;border-radius:3px;background:#8a8a8a}
.social svg{display:block}
.footer-col{position:absolute;top:6px;font-size:11px;color:var(--footer-text);line-height:13.5px;letter-spacing:.3px}
.footer-col h5{font-weight:400;font-size:12px;margin-bottom:8px}
.copyright{position:absolute;left:31px;top:93px;font-size:8px;color:#333}
</style>
</head>
<body>
<header class="site-header">
  <svg class="header-shapes" width="976" height="170" aria-hidden="true">
    <defs>
      <linearGradient id="tabShade" x1="0" x2="1" y1="0" y2="0">
        <stop offset="0" stop-color="#2c3444"/>
        <stop offset="0.6" stop-color="#1c222c"/>
        <stop offset="1" stop-color="#3a3f48"/>
      </linearGradient>
    </defs>
    <path d="M18 48 Q18 42 26 41 L924 12 Q934 12 935 22 L937 150 L26 150 Z" fill="url(#tabShade)"/>
  </svg>
  <nav class="main-nav">
    <a style="left:495px">About us</a>
    <a style="left:620px;top:3px">Contact</a>
    <a style="left:737px">Jobs</a>
    <a style="left:834px;top:3px">Web Shop</a>
  </nav>
  <div class="brand-bar">
    <div class="stadium-photo" role="img" aria-label="Photograph of a floodlit stadium at night"></div>
    <div class="brand-name">Velmora Athletics</div>
  </div>
</header>

<div class="content-frame"></div>

<section class="services">
  <article class="service" style="top:18px">
    <h2>Sports Media Services</h2>
    <p>Ultimate Sports Intelligence for journalists.</p>
    <a class="read-more">read more..</a>
    <div class="partners"><div class="partner-badge"><span></span></div><div class="partner-badge"><span></span></div><div class="partner-badge"><span></span></div></div>
  </article>
  <div class="service-divider" style="top:105px"></div>
  <article class="service" style="top:120px">
    <h2>Sports Content Services</h2>
    <p>Fastest richest reliable sports statistics &amp; news channel</p>
    <a class="read-more">read more..</a>
    <div class="partners"><div class="partner-badge"><span></span></div><div class="partner-badge"><span></span></div><div class="partner-badge"><span></span></div></div>
  </article>
  <div class="service-divider" style="top:207px"></div>
  <article class="service" style="top:222px">
    <h2>Sports Event Services</h2>
    <p>The best media Support an fevent organizer can get</p>
    <a class="read-more">read more..</a>
    <div class="partners"><div class="partner-badge"><span></span></div><div class="partner-badge"><span></span></div><div class="partner-badge"><span></span></div></div>
  </article>
  <div class="service-divider" style="top:311px"></div>
  <article class="service" style="top:322px">
    <h2>Sports Federation Services</h2>
    <p>One stop shop media solutions for federations.</p>
    <a class="read-more">read more..</a>
    <div class="partners"><div class="partner-badge"><span></span></div><div class="partner-badge"><span></span></div><div class="partner-badge"><span></span></div></div>
  </article>
</section>

<section class="headlines">
  <article class="news-item" style="top:30px">
    <div class="news-photo" role="img" aria-label="Photograph of a tennis player celebrating on court" style="background:linear-gradient(135deg,#6b5a4a,#3e66a8 60%,#a9b6c8)"></div>
    <h3>Quisque vitae pede.</h3>
    <p>Quisque vitae pede. Nam et augue. Sed a elit. Ut vel massa. Suspendisse nibh pede, ultrices vitae,ultrices nec, mollis non nibh.Quisque vitae pede. Nam et augue. Sed a elit Ut vel massa. Suspendisse nibh pede, ultrices vitae,ultrices nec, mollis non nibh. Quisque vitae pede. Nam et augue. Sed a elit. Ut vel massa. Suspendisse nibh pede, ultrices vitae ultrices nec, mollis non nibh.Quisque vitae pede. Nam et augue. Sed a elit. Ut vel massa. Suspendisse nibh pede, ultrices vitae ultrices nec, mollis non nibh...</p>
  </article>
  <article class="news-item" style="top:183px">
    <div class="news-photo" role="img" aria-label="Photograph of a tennis player returning a ball" style="background:linear-gradient(135deg,#1d4fa0,#2c6ac4 55%,#0f2c5c)"></div>
    <h3>Quisque vitae pede.</h3>
    <p>Quisque vitae pede. Nam et augue. Sed a elit. Ut vel massa. Suspendisse nibh pede, ultrices vitae,ultrices nec, mollis non nibh.Quisque vitae pede. Nam et augue. Sed a elit Ut vel massa. Suspendisse nibh pede, ultrices vitae,ultrices nec, mollis non nibh. Quisque vitae pede. Nam et augue. Sed a elit. Ut vel massa. Suspendisse nibh pede, ultrices vitae ultrices nec, mollis non nibh.Quisque vitae pede. Nam et augue. Sed a elit. Ut vel massa. Suspendisse nibh pede, ultrices vitae ultrices nec, mollis non nibh...</p>
  </article>
  <article class="news-item" style="top:328px">
    <div class="news-photo" role="img" aria-label="Photograph of a player with an umbrella on a rainy court" style="background:linear-gradient(180deg,#e4e6ea,#a8adb5 60%,#6f747c)"></div>
    <h3>Quisque vitae pede.</h3>
    <p>Quisque vitae pede. Nam et augue. Sed a elit. Ut vel massa. Suspendisse nibh pede, ultrices vitae,ultrices nec, mollis non nibh.Quisque vitae pede. Nam et augue. Sed a elit Ut vel massa. Suspendisse nibh pede, ultrices vitae,ultrices nec, mollis non nibh. Quisque vitae pede. Nam et augue. Sed a elit. Ut vel massa. Suspendisse nibh pede, ultrices vitae ultrices nec, mollis non nibh.Quisque vitae pede. Nam et augue. Sed a elit. Ut vel massa. Suspendisse nibh pede, ultrices vitae ultrices nec, mollis non nibh...</p>
  </article>

  <aside class="events">
    <h3>EVENTS<br>we are involved in<br>start in:</h3>
    <div class="event">
      <h4>Quisque vitae pede.</h4>
      <p>Quisque vitae pede. Nam et augue. Sed a elit. Ut vel massa. Suspendisse nibh pede, ultrices vitae,ultrices nec, mollis non nibh.Quisque vitae pede.</p>
    </div>
    <div class="event">
      <h4>Quisque vitae pede.</h4>
      <p>Quisque vitae pede. Nam et augue. Sed a elit. Ut vel massa. Suspendisse nibh pede, ultrices vitae ultrices nec, mollis non nibh. Quisque vitae pede. Nam et augue. Sed a elit. Ut vel massa.</p>
    </div>
    <div class="event">
      <h4>Quisque vitae pede.</h4>
      <p>Quisque vitae pede. Nam et augue. Sed a elit. Ut vel massa. Suspendisse nibh pede, ultrices vitae ultrices nec, mollis non nibh.</p>
    </div>
  </aside>
</section>

<footer class="site-footer">
  <div class="follow">Follow us</div>
  <div class="social">
    <span></span><span></span><span></span>
    <svg width="26" height="21" viewBox="0 0 26 21" aria-label="Email"><rect x="1" y="2" width="24" height="17" fill="#f4f4f4" stroke="#9a9a9a"/><path d="M1 2 L13 12 L25 2" fill="none" stroke="#9a9a9a"/></svg>
  </div>
  <div class="footer-col" style="left:208px"><h5>Nam et augue</h5>Lorem ipsum<br>Suspendisse nibh<br>Lorem ipsum<br>Quisque vitae pede</div>
  <div class="footer-col" style="left:386px"><h5>Nam et augue</h5>Lorem ipsum<br>Suspendisse nibh<br>Lorem ipsum<br>Quisque vitae pede</div>
  <div class="footer-col" style="left:564px"><h5>Nam et augue</h5>Lorem ipsum<br>Suspendisse nibh<br>Lorem ipsum<br>Quisque vitae pede</div>
  <div class="footer-col" style="left:743px"><h5>Nam et augue</h5>Lorem ipsum<br>Suspendisse nibh<br>Lorem ipsum<br>Quisque vitae pede</div>
  <div class="copyright">Copyright &copy; 2011 All rights reserved</div>
</footer>
</body>
</html>
```